Training material templates, Word and PowerPoint

I conduct management training for executive level clients. I am looking to develop a template for the training materials that has a consistent high quality look. These training materials include participant handouts and workbooks, training information sheets and PowerPoint presentations.
I have previously used lumen yard to design a logo, business cards and letterheads, which are attached as examples.

Target Market(s)

Professionals

Requirements
Nice to have
• My preference for body text in Word documents is Calibri 11pt, with headings being a compatible font.
Preference is also for text in Word documents to be single height, with 6 point spacing before and after

```html
<!DOCTYPE html>
<html lang="en">
<head>
<meta charset="utf-8">
<title>Harlow Consulting – Training Material Templates</title>
<link rel="stylesheet" href="https://fonts.googleapis.com/css2?family=Open+Sans:wght@300;400;600;700&display=swap">
<style>
:root{
  --stage:#3a3a3a;
  --blue:#29a8e0;
  --blue-soft:#5bbde8;
  --ink:#555a60;
  --ink-dark:#2f3336;
  --grey:#8c8f92;
  --rule:#d6d9dc;
  --row:#e6e7e8;
  --paper:#ffffff;
}
*{box-sizing:border-box;margin:0;padding:0}
html,body{width:1200px;height:765px;overflow:hidden;background:var(--stage);font-family:"Open Sans",Arial,sans-serif;color:var(--ink)}
.canvas{position:relative;width:1200px;height:765px}
.sheet,.slide{position:absolute;background:var(--paper);overflow:hidden}
.abs{position:absolute}

/* brand name lockup */
.brand{position:absolute;display:flex;align-items:center;gap:3px;color:var(--blue);font-weight:600;letter-spacing:.12em;white-space:nowrap;line-height:1}
.brand i{display:block;background:var(--blue)}

/* photo placeholders */
.photo-building{background:linear-gradient(115deg,#b9c6c6 0%,#dfe6e6 35%,#f3f6f7 65%,#e7ecee 100%)}
.photo-blue{background:linear-gradient(115deg,#4fb2e2 0%,#5fbde8 50%,#4bb0e0 100%)}

/* A4 documents */
.sheet{width:155px;height:221px}
.doc-head .brand{left:10px;top:8px;font-size:6.5px}
.doc-head .brand i{width:6px;height:6px}
.doc-head .tagline{position:absolute;right:12px;top:11px;font-size:2.6px;color:var(--blue);letter-spacing:.03em}
.doc-head .rule{position:absolute;left:10px;right:12px;top:19px;height:.5px;background:var(--rule)}
.doc-head .rule::before{content:"";position:absolute;left:0;top:-.3px;width:47px;height:1px;background:var(--blue)}
.doc-foot{position:absolute;left:13px;right:12px;bottom:5px;height:14px;border-top:.5px solid var(--rule)}
.doc-foot p{font-size:2.6px;color:var(--blue);line-height:4.2px;padding-top:2px}
.doc-foot .brand{right:0;top:4px;font-size:4.6px}
.doc-foot .brand i{width:4px;height:4px}
.sheet .base{position:absolute;left:0;right:0;bottom:0;height:1.5px;background:var(--blue)}

.cover-band{position:absolute;left:0;top:134px;width:155px;height:50px;background:var(--blue);color:#fff;padding:6px 16px}
.cover-band .kind{font-size:8px;font-weight:300;line-height:9px}
.cover-band .name{font-size:11px;font-weight:700;line-height:11px}
.cover-band .bar{width:29px;height:1.5px;background:#fff;margin:4px 0 5px}
.cover-band .date{font-size:3.2px;line-height:4.6px}
.cover-info{position:absolute;left:14px;top:190px;font-size:3.8px;color:var(--blue);line-height:6px}
.cover-info b{font-weight:700}

.body-title{position:absolute;left:13px;top:31px;font-size:8px;font-weight:700;color:var(--blue)}
.sub-title{position:absolute;left:13px;font-size:4px;font-weight:700;color:var(--ink-dark)}
.fine{position:absolute;left:13px;width:124px;font-size:2.6px;line-height:4.1px;color:var(--grey)}
.data-table{position:absolute;left:13px;top:110px;width:124px;border-collapse:collapse;font-size:2.7px;color:var(--grey)}
.data-table th{background:var(--blue);color:#fff;font-weight:400;height:8px;text-align:center;border-right:.5px solid #fff}
.data-table td{height:14.5px;padding:1px 2px;line-height:3.6px;border-right:.5px solid var(--rule);vertical-align:middle}
.data-table tr:nth-child(even) td{background:var(--row)}
.data-table{border:.5px solid var(--rule)}

.toc{position:absolute;left:21px;top:59px;width:117px;font-size:2.6px;color:var(--grey);list-style:none}
.toc li{display:flex;align-items:center;height:4.65px}
.toc li::after{content:"";order:1;flex:1;border-bottom:.4px solid #b8bbbe;margin:0 1.5px}
.toc li span:last-child{order:2}
.toc li.main{color:var(--blue);font-weight:700}
.toc li.sub{padding-left:3px}

/* slides */
.slide{width:268px;height:201px}
.slide .base{position:absolute;left:0;right:0;bottom:0;height:2px;background:var(--blue)}
.slide .brand{font-size:12px}
.slide .brand i{width:10px;height:10px}
.title-tag{position:absolute;background:var(--blue);color:#fff;font-size:10px;padding:0 9px;height:13px;line-height:13px}
.slide-copy{position:absolute;font-size:4.4px;line-height:9.1px}
.head-band{position:absolute;left:0;top:0;width:268px;height:34px;background:var(--blue);color:#fff;font-size:17px;padding:6px 0 0 15px;white-space:nowrap}
.head-rule{position:absolute;left:0;top:34px;width:268px;height:2px;background:#9a9da0}
.contents{position:absolute;left:54px;top:96px;width:150px;list-style:none;font-size:8px;color:var(--grey)}
.contents li{display:flex;justify-content:space-between;height:15.7px}
.bullets{position:absolute;top:143px;list-style:none;font-size:2.6px;color:var(--ink-dark)}
.bullets li{display:flex;align-items:center;gap:6px;height:9.5px}
.bullets li::before{content:"";width:4.5px;height:4.5px;border-radius:50%;background:var(--ink-dark);flex:none}
</style>
</head>
<body>
<main class="canvas">

  <!-- Workbook cover -->
  <section class="sheet" style="left:90px;top:76px" aria-label="Workbook cover">
    <div class="abs photo-building" role="img" aria-label="Photograph of a white modern building facade with vertical fins against a pale sky" style="left:0;top:0;width:155px;height:134px"></div>
    <div class="brand" style="left:67px;top:22px;font-size:11px"><i style="width:9px;height:9px"></i>HARLOW</div>
    <div class="cover-band">
      <p class="kind">Workbook</p>
      <p class="name">Exemple</p>
      <div class="bar"></div>
      <p class="date">Prepared date :<br>03-25-2021</p>
    </div>
    <div class="cover-info">
      <b>Adress</b><br>
      12 Alder Row , Brookfield ,USA<br>
      <span style="display:inline-block;margin-top:6px">www.harlowlearning.com</span><span style="margin-left:12px">+1 555 014 2290</span>
    </div>
  </section>

  <!-- Letterhead page -->
  <section class="sheet" style="left:253px;top:76px" aria-label="Blank letterhead page">
    <div class="doc-head"><div class="brand"><i></i>HARLOW</div><p class="tagline">CONSLTING LEADERS</p><div class="rule"></div></div>
    <div class="doc-foot"><p>12 Alder Row , Brookfield ,USA<br>www.harlowlearning.com</p><div class="brand"><i></i>HARLOW</div></div>
    <div class="abs" style="left:13px;bottom:2px;font-size:2.6px;color:var(--blue)">+1 555 014 2290</div>
    <div class="base"></div>
  </section>

  <!-- Content page -->
  <section class="sheet" style="left:90px;top:336px" aria-label="Document body page">
    <div class="doc-head"><div class="brand"><i></i>HARLOW</div><p class="tagline">CONSLTING LEADERS</p><div class="rule"></div></div>
    <h1 class="body-title">Primary title</h1>
    <h2 class="sub-title" style="top:47px">Secondary title</h2>
    <p class="fine" style="top:54px">Lorem ipsum dolor sit amet, consectetur adipiscing elit. Non mi, nec massa eleifend dui pharetra, vel risus, at. Est egestas purus donec nunc. Amet id massa, in sed nisi amet pharetra. Adipiscing velit et enim scelerisque velit interdum morbi malesuada quis. In blandit lacus, elementum tincidunt ultricies id. Ipsum tellus id eget non ipsum iaculis. Consectetur nunc interdum purus metus pretium integer tortor diam mattis. Id lorem facilisis quam auctor ullamcorper est, nibh sed. Amet aliquam ut dictum fermentum. Sit posuere semper sed euismod. Nunc sagittis amet sapien, nec sed nisi odio scelerisque urna. Suspendisse eu, et at mattis quisque duis. Eu porta sit sed sem. Placerat adipiscing turpis magnis ut.</p>
    <h2 class="sub-title" style="top:100px">Table exemple</h2>
    <table class="data-table">
      <tr><th>Case one title</th><th>Description</th><th>Scondary description</th></tr>
      <tr><td>Lorem ipsum dolor</td><td>Id lorem facilisis quam auctor ullamcorper est</td><td>Id lorem facilisis quam auctor ullamcorper est</td></tr>
      <tr><td>Lorem ipsum dolor</td><td>Id lorem facilisis quam auctor ullamcorper est</td><td>Id lorem facilisis quam auctor ullamcorper est</td></tr>
      <tr><td>Lorem ipsum dolor</td><td>Id lorem facilisis quam auctor ullamcorper est</td><td>Id lorem facilisis quam auctor ullamcorper est</td></tr>
      <tr><td>Lorem ipsum dolor</td><td>Id lorem facilisis quam auctor ullamcorper est</td><td>Id lorem facilisis quam auctor ullamcorper est</td></tr>
      <tr><td>Lorem ipsum dolor</td><td>Id lorem facilisis quam auctor ullamcorper est</td><td>Id lorem facilisis quam auctor ullamcorper est</td></tr>
    </table>
    <div class="doc-foot"><p>12 Alder Row , Brookfield ,USA<br>www.harlowlearning.com</p><div class="brand"><i></i>HARLOW</div></div>
    <div class="abs" style="left:13px;bottom:2px;font-size:2.6px;color:var(--blue)">+1 555 014 2290</div>
    <div class="base"></div>
  </section>

  <!-- Table of contents page -->
  <section class="sheet" style="left:261px;top:336px" aria-label="Table of contents page">
    <div class="doc-head"><div class="brand"><i></i>HARLOW</div><p class="tagline">CONSLTING LEADERS</p><div class="rule"></div></div>
    <h2 class="sub-title" style="left:22px;top:38px">Tabe of contents</h2>
    <p class="fine" style="left:22px;top:45px;width:115px">Lorem ipsum dolor sit amet, consectetur adipiscing elit.Lorem ipsum dolor sit amet, consectetur adipiscing elit.</p>
    <ul class="toc">
      <li class="main"><span>1-Introduction</span><span>08</span></li>
      <li class="main"><span>2-Topic one</span><span>08</span></li>
      <li class="sub"><span>2.1-Secondary Topic one</span><span>10</span></li>
      <li class="sub"><span>2.2 -Secondary Topic two</span><span>11</span></li>
      <li class="sub"><span>2.3 -Sec ondary Topic three</span><span>12</span></li>
      <li class="main"><span>3-Topic three</span><span>13</span></li>
      <li class="sub"><span>2.1-Secondary Topic one</span><span>14</span></li>
      <li class="sub"><span>2.2 -Secondary Topic two</span><span>15</span></li>
      <li class="sub"><span>2.3 -Sec ondary Topic three</span><span>17</span></li>
      <li class="sub"><span>2.1-Secondary Topic one</span><span>21</span></li>
      <li class="sub"><span>2.2 -Secondary Topic two</span><span>22</span></li>
      <li class="sub"><span>2.3 -Sec ondary Topic three</span><span>23</span></li>
      <li class="main"><span>3-Topic three</span><span>25</span></li>
      <li class="sub"><span>2.1-Secondary Topic one</span><span>27</span></li>
      <li class="sub"><span>2.2 -Secondary Topic two</span><span>29</span></li>
      <li class="sub"><span>2.3 -Sec ondary Topic three</span><span>31</span></li>
      <li class="sub"><span>2.1-Secondary Topic one</span><span>35</span></li>
      <li class="sub"><span>2.2 -Secondary Topic two</span><span>38</span></li>
      <li class="sub"><span>2.3 -Sec ondary Topic three</span><span>&nbsp;</span></li>
      <li class="main"><span>3-Topic three</span><span>40</span></li>
      <li class="sub"><span>2.1-Secondary Topic one</span><span>42</span></li>
      <li class="sub"><span>2.2 -Secondary Topic two</span><span>45</span></li>
      <li class="sub"><span>2.3 -Sec ondary Topic three</span><span>48</span></li>
      <li class="sub"><span>2.1-Secondary Topic one</span><span>54</span></li>
      <li class="sub"><span>2.2 -Secondary Topic two</span><span>58</span></li>
      <li class="sub"><span>2.3 -Sec ondary Topic three</span><span>61</span></li>
    </ul>
    <div class="doc-foot"><p>12 Alder Row , Brookfield ,USA<br>www.harlowlearning.com</p><div class="brand"><i></i>HARLOW</div></div>
    <div class="abs" style="left:13px;bottom:2px;font-size:2.6px;color:var(--blue)">+1 555 014 2290</div>
    <div class="base"></div>
  </section>

  <!-- Slide: title with photo -->
  <section class="slide" style="left:553px;top:42px" aria-label="Title slide">
    <div class="abs photo-building" role="img" aria-label="Photograph of a white modern building facade with vertical fins against a pale sky" style="left:0;top:0;width:268px;height:139px"></div>
    <div class="title-tag" style="left:40px;top:43px;width:146px;padding-left:5px;background:rgba(41,168,224,.85)">Prestation Titles</div>
    <p class="slide-copy" style="left:40px;top:61px;width:146px;height:42px;padding:1px 2px;background:rgba(41,168,224,.75);color:#fff">Lorem ipsum dolor sit amet, consectetur adipiscing elit. Quam sollicitudin vitae, elementum vel et quam donec amet. A amet feugiat scelerisque integer.</p>
    <div class="brand" style="left:29px;top:165px"><i></i>HARLOW</div>
    <p class="abs" style="left:162px;top:166px;font-size:7.5px;color:var(--grey)">www.harlowlearning.com</p>
    <div class="base"></div>
  </section>

  <!-- Slide: title with text -->
  <section class="slide" style="left:846px;top:42px" aria-label="Title and text slide">
    <div class="abs photo-building" role="img" aria-label="Photograph of a white modern building facade fading into white" style="left:0;top:0;width:100px;height:199px;background:linear-gradient(90deg,#c4cfcf 0%,#e6ecec 45%,rgba(255,255,255,0) 100%)"></div>
    <div class="title-tag" style="left:118px;top:53px">Prestation Titles</div>
    <p class="slide-copy" style="left:118px;top:76px;width:146px;color:var(--grey)">Lorem ipsum dolor sit amet, consectetur adipiscing elit. Quam sollicitudin vitae, elementum vel et quam donec amet. A amet feugiat scelerisque integer. Id rhoncus ornare cras mattis consectetur porta velit purus cursus. Quis tortor nisl ultrices magna. Tristique elementum odio gravida sagittis congue vestibulum in cursus nulla. Nulla accumsan, tincidunt porta diam tincidunt. Sit dictum velit elit at sit. Ligula dapibus auctor semper imperdiet placerat quis. Malesuada sem quam consequat vitae. Proin massa volutpat sollicitudin urna non.</p>
    <div class="brand" style="left:182px;top:176px"><i></i>HARLOW</div>
    <div class="abs" style="left:0;bottom:0;width:145px;height:2px;background:var(--blue)"></div>
    <div class="abs" style="left:145px;bottom:0;width:123px;height:2px;background:#8c8f92"></div>
  </section>

  <!-- Slide: section break -->
  <section class="slide" style="left:553px;top:282px;background:var(--blue)" aria-label="Section break slide">
    <h2 class="abs" style="left:53px;top:52px;font-size:18px;font-weight:400;color:#fff">Section Break</h2>
    <p class="slide-copy" style="left:53px;top:78px;width:170px;color:#fff">Lorem ipsum dolor sit amet, consectetur adipiscing elit. Quam sollicitudin vitae, elementum vel et quam donec amet. A amet feugiat scelerisque integer. Id rhoncus ornare cras mattis consectetur porta velit purus cursus. Quis tortor nisl ultrices magna. Tristique elementum odio gravida sagittis congue vestibulum in cursus nulla. Nulla accumsan, tincidunt porta diam tincidunt. Sit dictum velit elit at sit. Ligula dapibus auctor semper imperdiet placerat quis. Malesuada sem quam consequat vitae. Proin massa volutpat sollicitudin urna non.</p>
  </section>

  <!-- Slide: thank you -->
  <section class="slide" style="left:846px;top:282px" aria-label="Closing slide">
    <div class="abs photo-blue" role="img" aria-label="Photograph of a modern building facade tinted blue" style="left:0;top:0;width:268px;height:139px"></div>
    <p class="abs" style="left:0;width:268px;top:36px;text-align:center;font-size:33px;font-weight:700;color:#fff;letter-spacing:.04em;line-height:1">Thank&nbsp;&nbsp;You</p>
    <p class="abs" style="left:75px;top:80px;font-size:18px;color:#fff">For listening</p>
    <div class="brand" style="left:16px;top:165px"><i></i>HARLOW</div>
    <div class="abs" style="left:137px;top:146px;font-size:6.8px;line-height:11.5px;color:var(--blue)"><b style="font-weight:700">Adress</b><br>12 Alder Row , Brookfield ,USA<br>www.harlowlearning.com<br><span style="display:inline-block;margin-top:3px">+1 555 014 2290</span></div>
    <div class="base"></div>
  </section>

  <!-- Slide: contents -->
  <section class="slide" style="left:554px;top:516px" aria-label="Contents slide">
    <h2 class="head-band" style="font-weight:400">Heading titles goes here</h2>
    <div class="head-rule"></div>
    <h3 class="abs" style="left:54px;top:62px;font-size:18px;font-weight:400;color:var(--blue)">Content</h3>
    <ul class="contents">
      <li><span>Title diaporama one</span><span>01</span></li>
      <li><span>Title diaporama two</span><span>05</span></li>
      <li><span>Title diaporama three</span><span>08</span></li>
      <li><span>Title diaporama four</span><span>10</span></li>
    </ul>
    <div class="brand" style="left:8px;top:179px"><i></i>HARLOW</div>
    <div class="base"></div>
  </section>

  <!-- Slide: charts -->
  <section class="slide" style="left:846px;top:516px" aria-label="Chart slide">
    <h2 class="head-band" style="font-weight:400">Heading titles goes here</h2>
    <div class="head-rule"></div>
    <svg class="abs" style="left:0;top:40px" width="268" height="100" viewBox="0 0 268 100" font-family="Open Sans, sans-serif">
      <g font-size="3.2" fill="#2f3336" text-anchor="end">
        <text x="14" y="17">250</text><text x="14" y="30.6">200</text><text x="14" y="44.2">150</text>
        <text x="14" y="57.8">100</text><text x="14" y="71.4">50</text><text x="14" y="85">0</text>
      </g>
      <g stroke="#e3e4e5" stroke-width=".4">
        <line x1="18" y1="16" x2="115" y2="16"/><line x1="18" y1="29.6" x2="115" y2="29.6"/><line x1="18" y1="43.2" x2="115" y2="43.2"/><line x1="18" y1="56.8" x2="115" y2="56.8"/><line x1="18" y1="70.4" x2="115" y2="70.4"/>
      </g>
      <line x1="18" y1="14" x2="18" y2="84" stroke="#2f3336" stroke-width=".6"/>
      <line x1="18" y1="84" x2="115" y2="84" stroke="#2f3336" stroke-width=".6"/>
      <g>
        <rect x="29" y="35" width="6" height="49" fill="#2f3336"/><rect x="36" y="59.5" width="6" height="24.5" fill="#8c8f92"/><rect x="43" y="44.6" width="6" height="39.4" fill="var(--blue)"/>
        <rect x="58" y="16" width="6" height="68" fill="#2f3336"/><rect x="65" y="44.6" width="6" height="39.4" fill="#8c8f92"/><rect x="72" y="56.8" width="6" height="27.2" fill="var(--blue)"/>
        <rect x="87" y="35" width="6" height="49" fill="#2f3336"/><rect x="94" y="56.8" width="6" height="27.2" fill="#8c8f92"/><rect x="101" y="24.2" width="6" height="59.8" fill="var(--blue)"/>
      </g>
      <g font-size="5" font-weight="700" fill="#2f3336" text-anchor="middle">
        <text x="39" y="92">2001</text><text x="68" y="92">2002</text><text x="97" y="92">2002</text>
      </g>
      <g transform="rotate(-90 214 52)" fill="none" stroke-width="17">
        <circle cx="214" cy="52" r="35" stroke="#8c8f92" stroke-dasharray="110 110"/>
        <circle cx="214" cy="52" r="35" stroke="#2f3336" stroke-dasharray="0 110 44 66"/>
        <circle cx="214" cy="52" r="35" stroke="var(--blue)" stroke-dasharray="0 154 66 0"/>
      </g>
      <g font-size="4" font-weight="700" fill="#fff">
        <text x="185" y="36">36%</text><text x="243" y="57">50%</text><text x="187" y="75">20%</text>
      </g>
    </svg>
    <ul class="bullets" style="left:11px">
      <li>Lorem ipsum dolor sit amet, consectetur adipiscing elit. Quam sollicitudin</li>
      <li>Id rhoncus ornare cras mattis consectetur porta velit purus cursus.</li>
      <li>Tristique elementum odio gravida sagittis congue vestibulum in cursus nulla.</li>
    </ul>
    <ul class="bullets" style="left:143px">
      <li>Lorem ipsum dolor sit amet, consectetur adipiscing elit. Quam sollicitudin</li>
      <li>Id rhoncus ornare cras mattis consectetur porta velit purus cursus.</li>
      <li>Tristique elementum odio gravida sagittis congue vestibulum in cursus nulla.</li>
    </ul>
    <div class="base"></div>
  </section>

</main>
</body>
</html>
```